Modern card design needed for building development company

We are looking for a sharp modern new look for our business cards.
We are a New Zealand based company called TKV Ventures NZ LTD that specialises in subdividing large sections, housing and commercial buildings.
We have attached a photo of the current logo and would like to see it improved somehow as it looks a bit dated.
We are open to any colours.

Target Market(s)

Investors, Property buyers

Industry/Entity Type

Investment

Contact Information for Business Card

TKV VENTURES NZ LTD
www.tkvventuresnz.co.nz

Howard Pennick
Phone +64 21 843 192
Email hdpennick@fernmail.co.nz

Font styles to use
Serif
Sans Serif

Colors
0792cd
33a6d7
85cae6
6b449b
886aae
f04a50
ec1f27
f37122
f68d4d

Requirements
Must have
• Please try and make the logo more modern or if you have a similar one we would like to see it.

```html
<!DOCTYPE html>
<html lang="en">
<head>
<meta charset="utf-8">
<title>TKV Ventures NZ LTD – Business Card</title>
<link rel="stylesheet" href="https://fonts.googleapis.com/css2?family=Open+Sans:wght@400;600;700&display=swap">
<style>
  :root {
    --bg: #e4e2e0;
    --coral: #f04a50;
    --red: #ec1f27;
    --deep-red: #8e1b22;
    --white: #ffffff;
    --ink: #3a3a3a;
    --muted: #8a8a8a;
    --skyline-a: #f4f4f4;
    --skyline-b: #e9e9e9;
  }
  * { box-sizing: border-box; margin: 0; padding: 0; }
  html, body {
    width: 1200px; height: 997px; overflow: hidden;
    background: var(--bg);
    font-family: "Open Sans", Arial, sans-serif;
  }
  .card {
    position: absolute;
    width: 540px; height: 308px;
    box-shadow: 0 6px 18px rgba(0,0,0,.12);
  }
  /* Front */
  .card--front {
    left: 90px; top: 170px;
    background: var(--coral);
    color: var(--white);
    display: flex; flex-direction: column; align-items: center; justify-content: center;
  }
  .front__name {
    display: flex; align-items: center; gap: 14px;
    font-size: 28px; font-weight: 600; letter-spacing: .04em;
  }
  .front__square { width: 22px; height: 22px; border: 2px solid var(--white); }
  .front__web {
    margin-top: 34px;
    display: flex; align-items: center; gap: 12px;
    font-size: 11px; letter-spacing: .25em;
  }
  .front__rule { width: 40px; height: 1px; background: rgba(255,255,255,.7); }

  /* Back */
  .card--back {
    left: 570px; top: 520px;
    background: var(--white);
    overflow: hidden;
  }
  .back__skyline {
    position: absolute; left: 150px; top: 0; width: 300px; height: 308px;
    background: linear-gradient(180deg, var(--white) 0%, var(--skyline-a) 35%, var(--skyline-b) 100%);
  }
  .back__identity {
    position: absolute; left: 26px; top: 56px;
    border-left: 6px solid var(--red);
    padding-left: 12px;
  }
  .back__name { color: var(--red); font-weight: 700; font-size: 18px; line-height: 1.1; }
  .back__title { color: var(--muted); font-size: 11px; margin-top: 4px; }
  .back__contact {
    position: absolute; left: 32px; top: 170px;
    color: var(--ink); font-size: 11.5px; line-height: 1.45;
  }
  .back__address { margin-bottom: 6px; }
  .contact-row { display: flex; align-items: center; gap: 8px; }
  .contact-row svg { width: 11px; height: 11px; flex: none; }
  .back__brand {
    position: absolute; right: 22px; top: 110px;
    display: flex; align-items: center; gap: 10px;
    color: var(--deep-red); font-size: 15px; font-weight: 700; letter-spacing: .02em;
  }
  .back__square { width: 16px; height: 16px; background: var(--deep-red); }
</style>
</head>
<body>
  <section class="card card--front">
    <div class="front__name"><span class="front__square"></span>TKV VENTURES NZ LTD</div>
    <div class="front__web"><span class="front__rule"></span>www.tkvventuresnz.co.nz<span class="front__rule"></span></div>
  </section>

  <section class="card card--back">
    <div class="back__skyline" role="img" aria-label="Faint city skyline illustration behind the contact details"></div>

    <div class="back__identity">
      <div class="back__name">Howard Pennick</div>
      <div class="back__title">Title</div>
    </div>

    <div class="back__contact">
      <div class="back__address">PO BOX 48215<br>Takapuna, Auckland, New Zealand</div>
      <div class="contact-row">
        <svg viewBox="0 0 12 12" aria-hidden="true"><circle cx="6" cy="6" r="5.3" fill="none" stroke="#ec1f27" stroke-width="1.2"/><path d="M4 3.5l1 1-0.6 0.8c.4.9 1 1.5 1.9 1.9l.8-.6 1 1-.8.9c-2-.4-3.8-2.2-4.2-4.2z" fill="#ec1f27"/></svg>
        <span>+64 21 843 192</span>
      </div>
      <div class="contact-row">
        <svg viewBox="0 0 12 12" aria-hidden="true"><rect x="1" y="2.5" width="10" height="7" fill="#ec1f27"/><path d="M1 2.5l5 4 5-4" fill="none" stroke="#fff" stroke-width="1"/></svg>
        <span>hdpennick@fernmail.co.nz</span>
      </div>
      <div class="contact-row">
        <svg viewBox="0 0 12 12" aria-hidden="true"><circle cx="6" cy="6" r="5.3" fill="#ec1f27"/><path d="M0.7 6h10.6M6 0.7v10.6M6 0.7c-2.6 2.8-2.6 7.8 0 10.6M6 0.7c2.6 2.8 2.6 7.8 0 10.6" fill="none" stroke="#fff" stroke-width=".8"/></svg>
        <span>www.tkvventuresnz.co.nz</span>
      </div>
    </div>

    <div class="back__brand"><span class="back__square"></span>TKV VENTURES NZ LTD</div>
  </section>
</body>
</html>
```